Corwenna Foundation is a new grant making charity set up in the UK.

Having got a logo, we now need a website to go with it. We have worked out the text which people are going to need in order to then apply for grants. But having found out what we require they will probably need to go away and think about it.
We have to be careful of what images we use. So I have uploaded some images that we like. We are also going to be adding more pages almost immediately so need to think about the images for these.
I know basic wordpress so I will be able to add new pages/make alterations in future.
Updates
The website does need to be coded in Wordpress so that I can maintain it afterwards.
Corwenna
Brief changed to provide more money and we have also provided more possible pictures. And generally more explanation.
Target Market(s)
departments in universities, other charities doing work on relief of pain, people working in health service departments
Industry/Entity Type
Health Charity
Coding
Coded - Design and coding required
Number of Pages Required
4 page
Look and feel
Each slider illustrates characteristics of the customer's brand and the style your logo design should communicate.

```html
<!DOCTYPE html>
<html lang="en">
<head>
<meta charset="utf-8">
<title>Corwenna Foundation</title>
<link href="https://fonts.googleapis.com/css2?family=Raleway:wght@400;500;600&display=swap" rel="stylesheet">
<style>
:root{
  --brand:#0a6fbf;
  --band:#0070bd;
  --text:#333333;
  --muted:#777777;
  --footer:#8b8b8b;
  --white:#ffffff;
}
*{margin:0;padding:0;box-sizing:border-box}
html,body{width:849px;height:1200px;overflow:hidden;background:var(--white)}
body{font-family:'Raleway',sans-serif;color:var(--text);position:relative}
a{text-decoration:none;color:inherit}

.site-header{position:absolute;top:0;left:0;width:849px;height:70px}
.brand{position:absolute;left:114px;top:20px;display:flex;align-items:center;gap:7px;color:var(--brand);font-weight:600;font-size:19px;letter-spacing:.3px}
.brand-square{width:14px;height:14px;background:var(--brand)}
.header-mail{position:absolute;right:116px;top:13px;font-size:10px;color:var(--muted);display:flex;align-items:center;gap:7px}
.main-nav{position:absolute;right:116px;top:44px;display:flex;font-size:10px;color:var(--muted)}
.main-nav a{padding:0 16px;border-left:1px solid #ddd;line-height:14px}
.main-nav a:first-child{border-left:none}
.main-nav a:last-child{padding-right:0}
.main-nav .active{color:var(--brand)}

.hero{position:absolute;top:70px;left:0;width:849px;height:350px;overflow:hidden;border-bottom:2px solid #ddd}
.hero-photo{position:absolute;inset:0;background:linear-gradient(180deg,#3e63a8 0%,#7a8fc2 40%,#c6a9b6 75%,#d5a683 100%)}
.hero-text{position:absolute;left:116px;top:115px;color:var(--white)}
.hero-title{font-size:24px;font-weight:500;margin-bottom:8px}
.hero-sub{font-size:21px;font-weight:500;line-height:30px}
.slider-arrow{position:absolute;top:152px;width:27px;height:24px;background:#3a3a3a;border:2px solid #aaa;display:flex;align-items:center;justify-content:center}
.slider-arrow.prev{left:0}
.slider-arrow.next{right:0}

.intro{position:absolute;top:462px;left:0;width:849px;text-align:center;font-size:13px;line-height:23px}
.intro-brand{display:inline-flex;align-items:center;gap:7px;color:var(--brand);font-weight:600;font-size:18px;margin-bottom:18px}
.intro-reg{display:inline-block;margin-top:4px;color:var(--brand);border-bottom:1px solid var(--brand);line-height:19px}

.grants-band{position:absolute;top:630px;left:0;width:849px;height:195px;background:var(--band)}
.grants-image{position:absolute;left:114px;top:685px;width:279px;height:248px;background:radial-gradient(circle at 55% 45%,#ff7a2e 0%,#c9401b 30%,#3a2420 60%,#1b1b1b 100%)}
.grants-copy{position:absolute;left:423px;top:712px;width:310px;color:var(--white)}
.grants-copy h2{font-size:23px;font-weight:400;margin-bottom:10px}
.grants-copy p{font-size:13px;line-height:23px}
.know-more{position:absolute;left:423px;top:833px;font-size:13px;color:var(--brand);border-bottom:1px solid var(--brand);line-height:18px}
.faint-name{position:absolute;left:425px;top:875px;font-size:30px;font-weight:600;color:var(--brand);opacity:.08}

.site-footer{position:absolute;top:986px;left:0;width:849px;height:214px;background:var(--footer);color:var(--white)}
.footer-brand{position:absolute;left:114px;top:48px;display:flex;align-items:center;gap:8px;font-size:21px;font-weight:600}
.footer-brand .brand-square{background:var(--white);width:16px;height:16px}
.footer-nav{position:absolute;left:378px;top:55px;display:flex;font-size:10px}
.footer-nav a{padding:0 17px;border-left:1px solid #b0b0b0;line-height:14px}
.footer-nav a:first-child{border-left:none}
.contact-item{position:absolute;top:111px;display:flex;gap:9px;font-size:10px;line-height:16px}
.contact-icon{width:34px;height:34px;border:1px solid var(--white);display:flex;align-items:center;justify-content:center}
.contact-label{margin-top:1px}
.footer-rule{position:absolute;left:114px;top:172px;width:621px;border-top:1px solid #9e9e9e}
.copyright{position:absolute;top:182px;width:849px;text-align:center;font-size:10px;color:#eeeeee}
.copyright strong{font-weight:500;color:var(--white)}
</style>
</head>
<body>
<header class="site-header">
  <a class="brand" href="#"><span class="brand-square"></span>Corwenna Foundation</a>
  <div class="header-mail">
    <svg width="14" height="12" viewBox="0 0 14 12" fill="none" stroke="#0a6fbf" stroke-width="1"><rect x="1" y="3" width="12" height="8"/><path d="M1 3l6 5 6-5M3 3V1h8v2"/></svg>
    info@corwennafoundation.org
  </div>
  <nav class="main-nav">
    <a class="active" href="#">Home</a><a href="#">About Us</a><a href="#">Grants</a><a href="#">Contact Us</a>
  </nav>
</header>

<section class="hero">
  <div class="hero-photo" role="img" aria-label="Photo of two climbers in silhouette, one helping the other up a rocky summit against a sunset sky"></div>
  <div class="hero-text">
    <h1 class="hero-title">CORWENNA FOUNDATION</h1>
    <p class="hero-sub">We Get Funding For Pain<br>Research Or Education</p>
  </div>
  <a class="slider-arrow prev" href="#"><svg width="8" height="10" viewBox="0 0 8 10"><path d="M6 1L2 5l4 4" stroke="#fff" stroke-width="2" fill="none"/></svg></a>
  <a class="slider-arrow next" href="#"><svg width="8" height="10" viewBox="0 0 8 10"><path d="M2 1l4 4-4 4" stroke="#fff" stroke-width="2" fill="none"/></svg></a>
</section>

<section class="intro">
  <div class="intro-brand"><span class="brand-square"></span>Corwenna Foundation</div>
  <p>Corwenna Foundation is a grant making charity set up in the UK in 2021</p>
  <p>The main aim of Corwenna Foundation is to reduce the suffering caused by chronic pain.</p>
  <a class="intro-reg" href="#">Charity Registration Number 1187305</a>
</section>

<section class="grants">
  <div class="grants-band"></div>
  <div class="grants-image" role="img" aria-label="X-ray style illustration of a hunched figure with glowing areas of pain"></div>
  <div class="grants-copy">
    <h2>Grants</h2>
    <p>Grants will almost entirely be provided for research or education into pain management, or the prevention of pain.</p>
  </div>
  <a class="know-more" href="#">Know More</a>
  <div class="faint-name" aria-hidden="true">Corwenna Foundation</div>
</section>

<footer class="site-footer">
  <div class="footer-brand"><span class="brand-square"></span>Corwenna Foundation</div>
  <nav class="footer-nav">
    <a href="#">Home</a><a href="#">About Us</a><a href="#">Grants</a><a href="#">Contact Us</a>
  </nav>
  <div class="contact-item" style="left:114px">
    <span class="contact-icon"><svg width="14" height="12" viewBox="0 0 14 12" fill="none" stroke="#fff" stroke-width="1"><rect x="1" y="3" width="12" height="8"/><path d="M1 3l6 5 6-5M3 3V1h8v2"/></svg></span>
    <div class="contact-label">Email<br>info@corwennafoundation.org</div>
  </div>
  <div class="contact-item" style="left:395px">
    <span class="contact-icon"><svg width="14" height="14" viewBox="0 0 14 14" fill="none" stroke="#fff" stroke-width="1"><path d="M3 1l2 3-1.5 1.5a8 8 0 0 0 5 5L10 9l3 2-1.5 2.5C6 13 1 8 .5 2.5z"/></svg></span>
    <div class="contact-label">Phone<br>020-555-0148</div>
  </div>
  <div class="contact-item" style="left:599px">
    <span class="contact-icon"><span class="brand-square" style="background:#fff;width:12px;height:12px"></span></span>
    <div class="contact-label">Charity Registration<br>1187305</div>
  </div>
  <div class="footer-rule"></div>
  <p class="copyright">Copyright © 2021 <strong>Corwenna Foundation.</strong> All Rights Reserved.</p>
</footer>
</body>
</html>
```